Book cover design project
Tides of the Evening
Male Multi-Orgasmic Masturbation
This is a self-help sex guide aimed at men who want to learn how to masturbate to orgasm as often as they want to.
Health
The target audience is all sexually active men.
I have in mind a simple one-color design (blue?) making use of the alliterating three M's of the subtitle (MMM), which will also echo the sound of a person having pleasure ("mmm..") and the visual image of a man lying on his back with his knees bent. No pictures of people or objects please, just subtle graphic suggestion!

```html
<!DOCTYPE html>
<html lang="en">
<head>
<meta charset="utf-8">
<title>Tides of the Evening — Book Cover</title>
<link href="https://fonts.googleapis.com/css2?family=Open+Sans:wght@400;600&family=Dancing+Script:wght@500&display=swap" rel="stylesheet">
<style>
  :root {
    --cover-blue: #26508e;
    --cover-blue-deep: #1f4580;
    --paper: #ffffff;
    --backdrop: #f2f3f5;
    --tint: #e3eaf4;
  }
  * { margin: 0; padding: 0; box-sizing: border-box; }
  html, body {
    width: 1200px;
    height: 1000px;
    overflow: hidden;
    background: var(--backdrop);
  }
  .canvas {
    width: 1200px;
    height: 1000px;
    display: flex;
    align-items: center;
    justify-content: center;
  }
  .cover {
    position: relative;
    width: 600px;
    height: 900px;
    background: linear-gradient(160deg, var(--cover-blue) 0%, var(--cover-blue-deep) 100%);
    overflow: hidden;
    box-shadow: 0 2px 10px rgba(0,0,0,0.12);
  }
  .subtitle {
    position: absolute;
    top: 46px;
    left: 52px;
    font-family: "Open Sans", sans-serif;
    font-weight: 400;
    font-size: 15px;
    letter-spacing: 1.4px;
    color: var(--paper);
    text-transform: uppercase;
  }
  .title {
    position: absolute;
    top: 120px;
    left: 0;
    width: 100%;
    text-align: center;
    font-family: "Open Sans", sans-serif;
    font-weight: 400;
    color: var(--paper);
    line-height: 1;
  }
  .title-line {
    display: block;
    font-size: 104px;
    letter-spacing: -2px;
  }
  .title-link {
    display: block;
    font-family: "Dancing Script", cursive;
    font-size: 40px;
    margin: -4px 0 -10px 150px;
    letter-spacing: 0;
  }
  .title-line + .title-line { margin-top: -6px; }
  .figure-area {
    position: absolute;
    left: 0;
    bottom: 0;
    width: 600px;
    height: 360px;
  }
</style>
</head>
<body>
  <div class="canvas">
    <div class="cover">
      <p class="subtitle">Male Multi-Orgasmic Masturbation</p>
      <h1 class="title">
        <span class="title-line">tides</span>
        <span class="title-link">of the</span>
        <span class="title-line">evening</span>
      </h1>
      <svg class="figure-area" viewBox="0 0 600 360" role="img"
           aria-label="Line drawing of a reclining figure with bent knees formed by the letters mmm, in blue on white">
        <defs>
          <linearGradient id="figureTint" x1="0" y1="0" x2="0" y2="1">
            <stop offset="0" stop-color="#ffffff"/>
            <stop offset="1" stop-color="#e3eaf4"/>
          </linearGradient>
        </defs>
        <path d="M0 110 C 120 95, 220 80, 330 60 C 430 40, 520 30, 600 20 L600 360 L0 360 Z"
              fill="url(#figureTint)"/>
      </svg>
    </div>
  </div>
</body>
</html>
```